Constructor Company /Carpenter

We need a high quality design for a Brochure up to 8pages.Copmany does plastering, building houses, make renovation of houses.
Updates

Ich brauche zusätzliche Tage um durchzusehen

Target Market(s)

The Brochure is a high quality hand out for architects.

Industry/Entity Type

Construction Company

Font styles to use
Sans Serif

Colors

Designer to choose colors to be used in the design.

Requirements
Must have
• You can build the brochure like the website www.qelvorix.ch is built. The brochure needs to look clean, modern and professionell.
• The brochure need to have the same colors like website www.qelvorix.ch

```html
<!DOCTYPE html>
<html lang="de">
<head>
<meta charset="utf-8">
<title>Qelvorix Bau GmbH – Brochure Spread</title>
<link href="https://fonts.googleapis.com/css2?family=Poppins:wght@400;500;600;700&display=swap" rel="stylesheet">
<style>
  :root{
    --bg:#c9c9c9;
    --slate:#5c5e62;
    --slate-dark:#3d3f43;
    --blue:#1446a0;
    --blue-deep:#0c3580;
    --white:#ffffff;
    --text-soft:#e9eaec;
    --photo-light:#e4e6e8;
    --photo-mid:#b9bcbf;
  }
  *{box-sizing:border-box;margin:0;padding:0}
  html,body{width:1200px;height:2473px;overflow:hidden}
  body{background:var(--bg);font-family:"Poppins",sans-serif;position:relative}
  .spread{position:absolute;left:40px;top:830px;width:1120px;height:810px;display:flex;box-shadow:0 18px 40px rgba(0,0,0,.35)}
  .panel{position:relative;width:560px;height:100%;overflow:hidden}
  .back{background:var(--slate);color:var(--white)}
  .cover{background:var(--white)}
  .heading-box{display:block;width:max-content;margin:0 auto;border:1.5px dashed var(--white);padding:2px 14px;font-weight:600;font-size:17px;letter-spacing:.3px}
  .intro{position:absolute;top:22px;left:0;right:0;text-align:center}
  .intro p{font-size:11.5px;line-height:1.55;color:var(--text-soft);margin:10px auto 0;width:470px}
  .expect{position:absolute;top:170px;left:0;right:0}
  .benefits{display:flex;justify-content:center;gap:26px;margin-top:14px}
  .benefits ul{list-style:none}
  .benefits li,.benefit-single{display:flex;align-items:center;gap:7px;font-size:12px;color:var(--text-soft);line-height:22px}
  .divider{width:2px;background:var(--white);height:40px;margin-top:2px}
  .benefit-single{justify-content:center;margin-top:10px}
  .tick{width:12px;height:12px;flex:none}
  .workers-photo{position:absolute;left:0;top:300px;width:560px;height:310px;background:linear-gradient(180deg,var(--slate) 0%,#8b8f94 30%,#c7cacd 70%,#9ea2a6 100%)}
  .contact{position:absolute;left:0;right:0;bottom:0;height:200px;color:var(--white);text-align:center}
  .contact svg.band{position:absolute;left:0;top:-60px;width:560px;height:260px}
  .contact-body{position:relative;padding-top:34px}
  .contact h3{font-weight:600;font-size:20px}
  .contact .rule{width:52px;height:2px;background:var(--white);margin:6px auto 14px}
  .line{display:flex;justify-content:center;align-items:center;gap:8px;font-size:13px;margin-bottom:14px}
  .line strong{font-weight:600}
  .icon{width:14px;height:14px;flex:none}
  .url-small{font-size:14px}
  .brand{position:absolute;top:36px;left:0;right:0;display:flex;justify-content:center;align-items:center;gap:8px;z-index:3}
  .brand .mark{width:20px;height:20px;background:var(--blue-deep)}
  .brand span{font-size:20px;font-weight:500;color:var(--blue-deep)}
  .plaster-photo{position:absolute;inset:0 0 200px 0;background:linear-gradient(120deg,var(--photo-light) 0%,var(--photo-mid) 38%,#eceeef 55%,#e8a36a 78%,#d9773a 100%)}
  .cover-band{position:absolute;left:0;bottom:0;width:560px;height:360px}
  .circle{position:absolute;border-radius:50%;border:4px solid var(--white);z-index:2}
  .c1{left:38px;top:408px;width:150px;height:150px;background:linear-gradient(160deg,#f2f3f4,#a9b0b8)}
  .c2{left:160px;top:392px;width:170px;height:170px;background:linear-gradient(160deg,#eef0f2,#4f78b8)}
  .c3{left:306px;top:356px;width:210px;height:210px;background:linear-gradient(160deg,#2f7d86,#1c4f5c)}
  .headline{position:absolute;top:592px;left:0;right:0;text-align:center;color:var(--white);font-weight:700;font-size:33px;line-height:44px;letter-spacing:.5px;z-index:2}
  .url-box{position:absolute;left:145px;top:744px;width:270px;height:40px;background:var(--white);color:var(--slate-dark);font-size:20px;font-weight:500;display:flex;align-items:center;justify-content:center;z-index:2}
</style>
</head>
<body>
<main class="spread">
  <section class="panel back">
    <div class="intro">
      <span class="heading-box">Tradition and passion</span>
      <p>Our clients benefit from the experience we have gained over the past decades in our craft. We specialize in plasterer, facade and painting work.</p>
      <p>Our way of working allows a perfect on-time execution to the best quality.</p>
      <p>We are happy to hand you over our personal references on request.</p>
    </div>
    <div class="expect">
      <span class="heading-box">What you can expect from us:</span>
      <div class="benefits">
        <ul>
          <li><svg class="tick" viewBox="0 0 12 12"><circle cx="6" cy="6" r="5.2" fill="none" stroke="#fff"/><path d="M3.5 6.2l1.7 1.6 3.3-3.4" fill="none" stroke="#fff"/></svg>Qualitatively perfect work</li>
          <li><svg class="tick" viewBox="0 0 12 12"><circle cx="6" cy="6" r="5.2" fill="none" stroke="#fff"/><path d="M3.5 6.2l1.7 1.6 3.3-3.4" fill="none" stroke="#fff"/></svg>Adhering to the schedules</li>
        </ul>
        <div class="divider"></div>
        <ul>
          <li><svg class="tick" viewBox="0 0 12 12"><circle cx="6" cy="6" r="5.2" fill="none" stroke="#fff"/><path d="M3.5 6.2l1.7 1.6 3.3-3.4" fill="none" stroke="#fff"/></svg>Individual advice</li>
          <li><svg class="tick" viewBox="0 0 12 12"><circle cx="6" cy="6" r="5.2" fill="none" stroke="#fff"/><path d="M3.5 6.2l1.7 1.6 3.3-3.4" fill="none" stroke="#fff"/></svg>Detailed cost statement</li>
        </ul>
      </div>
      <div class="benefit-single"><svg class="tick" viewBox="0 0 12 12"><circle cx="6" cy="6" r="5.2" fill="none" stroke="#fff"/><path d="M3.5 6.2l1.7 1.6 3.3-3.4" fill="none" stroke="#fff"/></svg>Fair price-performance ratio</div>
    </div>
    <div class="workers-photo" role="img" aria-label="Photo of two painters in blue overalls working on a floor with paint cans"></div>
    <div class="contact">
      <svg class="band" viewBox="0 0 560 260" preserveAspectRatio="none">
        <path d="M0 20 Q280 120 560 10 L560 260 L0 260Z" fill="var(--slate-dark)"/>
        <path d="M0 40 Q280 140 560 30 L560 260 L0 260Z" fill="var(--blue)"/>
      </svg>
      <div class="contact-body">
        <h3>Get in touch</h3>
        <div class="rule"></div>
        <div class="line"><svg class="icon" viewBox="0 0 14 14"><path d="M7 13s-4.5-4.6-4.5-7.6a4.5 4.5 0 019 0C11.5 8.4 7 13 7 13z" fill="none" stroke="#fff"/><circle cx="7" cy="5.5" r="1.6" fill="none" stroke="#fff"/></svg>Qelvorix Bau GmbH Talackerweg 8 4147 Aesch</div>
        <div class="line"><svg class="icon" viewBox="0 0 14 14"><rect x="1" y="3" width="12" height="8" fill="none" stroke="#fff"/><path d="M1 3l6 5 6-5" fill="none" stroke="#fff"/></svg><strong>info@qelvorix.ch</strong> &nbsp;|&nbsp;<svg class="icon" viewBox="0 0 14 14"><path d="M3 1.5l2.2 2.6-1.2 1.6a8 8 0 004.3 4.3l1.6-1.2 2.6 2.2-1.3 1.5C6.5 12.5 1.5 7.5 1.5 2.8z" fill="none" stroke="#fff"/></svg><strong>079 000 11 22</strong></div>
        <div class="line url-small">www.qelvorix.ch</div>
      </div>
    </div>
  </section>
  <section class="panel cover">
    <div class="plaster-photo" role="img" aria-label="Photo of a plasterer in an orange cap applying plaster to a wall"></div>
    <div class="brand"><div class="mark"></div><span>Qelvorix Bau GmbH</span></div>
    <svg class="cover-band" viewBox="0 0 560 360" preserveAspectRatio="none">
      <path d="M0 110 Q300 150 560 40 L560 360 L0 360Z" fill="var(--blue)"/>
    </svg>
    <div class="circle c1" role="img" aria-label="Photo of a worker plastering a white wall"></div>
    <div class="circle c2" role="img" aria-label="Photo of a painter rolling paint on a wall"></div>
    <div class="circle c3" role="img" aria-label="Photo of facade workers on a glass building"></div>
    <h1 class="headline">IHR GIPSER AUS AESCH<br>IN BASEL<br>UND UMGEBUNG</h1>
    <div class="url-box">www.qelvorix.ch</div>
  </section>
</main>
</body>
</html>
```